Hollerby Consulting needs a quality & professional business card!

I am a recruitment and employment consultant from Brisbane, Australia and I had a fantastic logo organised by this community to I am hoping the business card will be the same.

I have attached the Hollerby consulting logo that ideally would feature on the back of the business card. There are a number of logos for you to use as you see fit. I would like the colour cheme to match that of the Hollerby Consulting logo. I also have a secondary company called Career Lantern Australia and I have included that logo as well. While it is an important part of the business I don't want this logo feature too predominantly as I am moving out of this space. This logo was created by myself and is of low quality. Feel free to use the icon and words however you want. The winning design will be smart, professional and eye-catching.

The information I am looking for in the business card is:
Name: Derek Hollerby
Position: Founder & Director
Phone: (07) 3156 4082
Mobile: 0418 672 051
Email: derek@careerlantern-example.com.au

Target Market(s)

Recruiters, government, large companies

Contact Information for Business Card

Name: Derek Hollerby
Phone: (07) 3156 4082
Mobile: 0418 672 051
Web: www.careerlantern-example.com.au

Font styles to use
Serif
Sans Serif

Requirements
Must have
• Hollerby Consulting Logo on reverse side
• Contact details on front side with smaller reference to Hollerby Consulting logo and Career Lantern Australia logo

```html
<!DOCTYPE html>
<html lang="en">
<head>
<meta charset="utf-8">
<title>Hollerby Consulting – Business Card</title>
<link rel="stylesheet" href="https://fonts.googleapis.com/css2?family=Montserrat:wght@400&family=Saira:wght@400;600&family=Noto+Serif:wght@700&display=swap">
<style>
  :root {
    --charcoal: #353535;
    --paper: #ffffff;
    --logo-grey: #d0cfcf;
    --ink: #2b2b2b;
    --blue: #0a8ac6;
    --green: #07a04a;
    --orange: #e0842f;
    --frame: #5a5a5a;
    --guide: #555555;
  }
  * { margin: 0; padding: 0; box-sizing: border-box; }
  html, body { width: 1106px; height: 1200px; overflow: hidden; background: var(--paper); }
  .sheet {
    position: relative; width: 1106px; height: 1200px;
    border: 1px solid var(--frame); background: var(--paper);
  }
  .card { position: absolute; left: 80px; width: 947px; overflow: hidden; }
  .safe-line { position: absolute; border: 2px dotted var(--guide); pointer-events: none; }

  /* Back side */
  .card-back { top: 15px; height: 568px; background: var(--charcoal); }
  .card-back .safe-line { left: 33px; top: 31px; width: 882px; height: 506px; border-color: #1e1e1e; }
  .back-brand { position: absolute; left: 95px; top: 186px; display: flex; align-items: center; gap: 48px; }
  .back-brand .brand-square { width: 150px; height: 150px; background: var(--logo-grey); }
  .back-brand .brand-name {
    font-family: "Montserrat", sans-serif; font-weight: 400; color: var(--logo-grey);
    line-height: 1;
  }
  .back-brand .brand-name .big { display: block; font-size: 78px; letter-spacing: 2px; }
  .back-brand .brand-name .small { display: block; font-size: 34px; letter-spacing: 23px; margin-top: 14px; }

  /* Front side */
  .card-front { top: 617px; height: 567px; background: var(--paper); border: 1.5px solid var(--frame); }
  .card-front .safe-line { left: 32px; top: 22px; width: 883px; height: 505px; }
  .front-brand { position: absolute; left: 79px; top: 50px; display: flex; align-items: center; gap: 22px; }
  .front-brand .brand-square { width: 70px; height: 70px; background: var(--ink); }
  .front-brand .brand-name { font-family: "Montserrat", sans-serif; font-weight: 400; color: var(--ink); line-height: 1; }
  .front-brand .brand-name .big { display: block; font-size: 42px; letter-spacing: 1px; }
  .front-brand .brand-name .small { display: block; font-size: 19px; letter-spacing: 12px; margin-top: 6px; }

  .person { position: absolute; right: 52px; top: 62px; text-align: right; font-family: "Saira", sans-serif; color: var(--ink); }
  .person .name { font-size: 28px; font-weight: 600; letter-spacing: 1px; line-height: 1; }
  .person .role { font-size: 15px; font-weight: 400; letter-spacing: 0.5px; margin-top: 4px; }

  .stripe { position: absolute; top: 205px; height: 193px; }
  .stripe.blue { left: 181px; width: 17px; background: var(--blue); }
  .stripe.green { left: 213px; width: 26px; background: var(--green); }
  .stripe.orange { left: 254px; width: 35px; background: var(--orange); }

  .contact-band { position: absolute; left: 301px; top: 205px; width: 646px; height: 194px; background: var(--charcoal); }
  .contact-list { list-style: none; position: absolute; left: 192px; top: 38px; font-family: "Saira", sans-serif; font-size: 18px; color: #fff; letter-spacing: 0.8px; }
  .contact-list li { display: flex; align-items: center; gap: 12px; height: 33px; }
  .contact-list svg { width: 20px; height: 20px; fill: none; stroke: #fff; stroke-width: 1.5; stroke-linecap: round; stroke-linejoin: round; }

  .secondary-brand { position: absolute; left: 53px; top: 418px; display: flex; align-items: center; gap: 16px; }
  .secondary-brand .brand-circle { width: 84px; height: 84px; border-radius: 50%; background: #111; }
  .secondary-brand .brand-name { font-family: "Noto Serif", serif; font-weight: 700; color: #111; line-height: 1.05; }
  .secondary-brand .brand-name .big { display: block; font-size: 38px; }
  .secondary-brand .brand-name .small { display: block; font-size: 20px; }
</style>
</head>
<body>
<main class="sheet">
  <section class="card card-back" aria-label="Card back">
    <div class="safe-line"></div>
    <div class="back-brand">
      <div class="brand-square"></div>
      <div class="brand-name"><span class="big">HOLLERBY</span><span class="small">CONSULTING</span></div>
    </div>
  </section>

  <section class="card card-front" aria-label="Card front">
    <div class="safe-line"></div>
    <div class="front-brand">
      <div class="brand-square"></div>
      <div class="brand-name"><span class="big">HOLLERBY</span><span class="small">CONSULTING</span></div>
    </div>

    <div class="person">
      <div class="name">Derek Hollerby</div>
      <div class="role">Founder &amp; Director</div>
    </div>

    <div class="stripe blue"></div>
    <div class="stripe green"></div>
    <div class="stripe orange"></div>

    <div class="contact-band">
      <ul class="contact-list">
        <li><svg viewBox="0 0 24 24"><path d="M5 3h4l2 5-3 2a12 12 0 0 0 6 6l2-3 5 2v4a2 2 0 0 1-2 2A18 18 0 0 1 3 5a2 2 0 0 1 2-2z"/></svg>(07) 3156 4082</li>
        <li><svg viewBox="0 0 24 24"><rect x="6" y="2" width="12" height="20" rx="2"/><path d="M6 5h12M6 18h12"/></svg>0418 672 051</li>
        <li><svg viewBox="0 0 24 24"><rect x="3" y="6" width="18" height="13" rx="1"/><path d="M3 7l9 7 9-7"/></svg>derek@careerlantern-example.com.au</li>
        <li><svg viewBox="0 0 24 24"><circle cx="12" cy="12" r="9"/><path d="M3 12h18M12 3a14 14 0 0 1 0 18M12 3a14 14 0 0 0 0 18"/></svg>www.careerlantern-example.com.au</li>
      </ul>
    </div>

    <div class="secondary-brand">
      <div class="brand-circle"></div>
      <div class="brand-name"><span class="big">Career Lantern</span><span class="small">Australia</span></div>
    </div>
  </section>
</main>
</body>
</html>
```